Zielgruppe
Unternehmensberatung; Zielgruppe sind professionelle Investoren aus dem Venture-Capital-Umfeld; daher ein hochwertiges und professionelles Erscheinungsbild, jedoch erfrischend und dynamisch (Start-up Umfeld)
Das Unternehmen ist ein Start-up und möchte Bestands- und möglichen Neukunden ein erfolgreiches neues Jahr wünschen und sich somit in das Gedächnis der potentiellen Kunden einprägen
Aufgabenstellung
Siehe Briefingpackage; im Wesentlichen die Gestaltung einer Neujahrskarte (Vorder- und Rückseite)

```html
<!DOCTYPE html>
<html lang="de">
<head>
<meta charset="utf-8">
<title>mivan7K – Neujahrskarte</title>
<link href="https://fonts.googleapis.com/css2?family=Merriweather:wght@400;700;900&family=Montserrat:wght@600&display=swap" rel="stylesheet">
<style>
  :root {
    --stage: #a7a7a7;
    --night: #0d1a26;
    --teal: #1b5566;
    --dusk: #c8612a;
    --ground: #231a18;
    --white: #ffffff;
    --ink: #1a1a1a;
    --brand-blue: #3d67b8;
    --suit: #22355c;
  }
  * { box-sizing: border-box; margin: 0; padding: 0; }
  html, body { width: 893px; height: 1200px; overflow: hidden; }
  body { background: var(--stage); position: relative; font-family: "Merriweather", Georgia, serif; }

  .card {
    position: absolute; left: 20px; top: 297px;
    width: 853px; height: 605px; overflow: hidden;
    box-shadow: 0 6px 18px rgba(0,0,0,.25);
  }
  .card__sky {
    position: absolute; inset: 0;
    background:
      radial-gradient(ellipse 38% 45% at 54% 30%, rgba(214,150,90,.55), transparent 70%),
      linear-gradient(180deg, var(--night) 0%, #10283a 45%, var(--teal) 70%, #3a6a74 80%, var(--dusk) 88%, var(--ground) 93%);
  }
  .card__team {
    position: absolute; left: 15px; top: 220px; width: 390px; height: 262px;
    background: linear-gradient(90deg, #15203a 0%, var(--suit) 40%, #1c2c4c 70%, var(--suit) 100%);
    border-radius: 60px 60px 0 0;
    opacity: .9;
  }

  .quote { position: absolute; left: 61px; top: 100px; color: var(--white); }
  .quote__text { font-size: 20px; line-height: 1.35; font-weight: 400; }
  .quote__author { font-size: 11px; margin-top: 12px; }

  .brand-mark {
    position: absolute; right: 40px; top: 58px;
    display: flex; align-items: center; gap: 6px;
    color: var(--white); font-size: 24px; font-weight: 700;
  }
  .brand-mark__square { width: 10px; height: 10px; background: var(--brand-blue); }

  .greeting { position: absolute; right: 45px; top: 135px; text-align: right; color: var(--white); font-weight: 700; line-height: .95; text-shadow: 0 2px 6px rgba(0,0,0,.35); }
  .greeting__small { font-size: 42px; display: block; }
  .greeting__big { font-size: 92px; font-weight: 900; display: block; letter-spacing: -2px; }

  .claim {
    position: absolute; right: 45px; top: 385px; width: 430px;
    text-align: right; color: var(--white); font-size: 12.5px; line-height: 1.55;
  }

  .footer-band { position: absolute; left: 399px; right: 0; bottom: 0; height: 62px; background: var(--ground); }
  .footer-band__url {
    position: absolute; left: 0; right: 40px; top: 23px; text-align: center;
    font-family: "Montserrat", Arial, sans-serif; font-size: 10.5px; letter-spacing: 6px; color: var(--white);
  }

  .info-panel { position: absolute; left: 0; bottom: 0; width: 400px; height: 124px; }
  .info-panel svg { position: absolute; inset: 0; }
  .info-panel__name { position: absolute; left: 34px; top: 46px; display: flex; align-items: center; gap: 6px; font-size: 22px; font-weight: 700; color: var(--ink); }
  .info-panel__square { width: 10px; height: 10px; background: var(--brand-blue); }
  .info-panel__tagline { position: absolute; left: 170px; width: 210px; top: 16px; text-align: center; font-size: 11.5px; line-height: 1.4; color: var(--ink); }
  .info-panel__button {
    position: absolute; left: 215px; top: 66px; width: 116px; height: 24px; border-radius: 12px;
    background: var(--brand-blue); color: var(--white);
    font-family: "Montserrat", Arial, sans-serif; font-size: 10.5px; line-height: 24px; text-align: center;
  }
</style>
</head>
<body>
  <section class="card">
    <div class="card__sky" role="img" aria-label="Foto: Feuerwerk am Nachthimmel über einer Hügellandschaft bei Abenddämmerung"></div>
    <div class="card__team" role="img" aria-label="Foto: vier Berater in Sakkos stehen nebeneinander"></div>

    <div class="quote">
      <p class="quote__text">Die zukunft hängt davon<br>ab was wir heute tun</p>
      <p class="quote__author">Aurelio Brandt</p>
    </div>

    <div class="brand-mark"><span>mivan7K</span><span class="brand-mark__square"></span></div>

    <h1 class="greeting">
      <span class="greeting__small">Happy</span>
      <span class="greeting__big">New</span>
      <span class="greeting__big">Year</span>
    </h1>

    <p class="claim">Die Firma <strong>mivan7K</strong> consulting unterstützt andere Firmen, die Performance zu steigern und auf das nächste Level zu heben</p>

    <div class="footer-band"><p class="footer-band__url">www.mivan7k.de</p></div>

    <div class="info-panel">
      <svg width="400" height="124" viewBox="0 0 400 124" aria-hidden="true">
        <path d="M0 0 H340 C372 0 392 22 400 60 V124 H0 Z" fill="#ffffff"/>
      </svg>
      <div class="info-panel__name"><span>mivan7K</span><span class="info-panel__square"></span></div>
      <p class="info-panel__tagline">Ihre Boutique-Beratung für Unternehmen in Sondersituationen</p>
      <div class="info-panel__button">www.mivan7k.de</div>
    </div>
  </section>
</body>
</html>
```